Design of a Web Development Agency

We're a web development agency (we do not offer design services). We'd like to get a new website up and running. We do custom web application development - large scale applications in the financial, healthcare, automotive, and other industries.

We need the following types of pages designed:
1) Homepage
2) Blog
3) Services page
4) Packages page
4) Generic content
5) Contact Us form.

The design should be consistent with our current icon. We're looking for a clean, corporate, brand. We'd like the design to expand on the concepts in the logo - the use of the electrical wiring motif / the colors / etc.

We offer the following services: 1) Corvel web hosting consulting, 2) custom application development, 3) eVN development, 4) Quillset development.

We offer packages in numbers of hours. We have about 3-4 tiers of services - the number of hours versus the monthly invoice total. For example, 5 hours per month of $500.00, for example.

Target Market(s)

Corporate clients

Industry/Entity Type

Electrical

Colors
acd036
33b7a4
33a6d7
3176b5
876aae
b768aa
fbee3e

Requirements
Must have
• Responsive / mobile friendly design.
• An email submitting form on the contact us page
Nice to have
• We'd like a bit of San Francisco to come through (where we're located)
• A plimbo map of our address on the contact us page
Should not have
• Excessive imagery. We don't have a lot of imagery, so we'd basically have to go out and find stock photography to put in it's place, which we just don't really want to do. All imagery should be supplied by the designer (we'll pay any copyright fees, if applicable, you just have to send us a list of the links to the imagery. Max budget would be $100-$200 on imagery, but preferably as little as possible).

```html
<!DOCTYPE html>
<html lang="en">
<head>
<meta charset="utf-8">
<title>Halden Web Works</title>
<link rel="stylesheet" href="https://fonts.googleapis.com/css2?family=Source+Sans+3:wght@400;600;700&family=Roboto:wght@400;500&display=swap">
<style>
:root{
  --lime:#d3df20;
  --lime-dark:#acd036;
  --olive:#7f9a12;
  --teal:#33b7a4;
  --blue:#3176b5;
  --sky:#33a6d7;
  --purple:#876aae;
  --pink:#b768aa;
  --ink:#1d1d1d;
  --text:#555;
  --muted:#888;
  --dark:#333;
  --rule:#ddd;
}
*{margin:0;padding:0;box-sizing:border-box}
html,body{width:787px;height:1200px;overflow:hidden;background:#fff}
body{position:relative;font-family:"Source Sans 3",Arial,sans-serif;color:var(--text)}
.abs{position:absolute}

/* header */
.brand{position:absolute;display:flex;align-items:center;gap:8px}
.brand-dot{width:52px;height:52px;border:2px solid var(--ink);border-radius:50%}
.brand-name{font-size:13px;color:var(--ink);font-weight:400}
.search{left:571px;top:9px;width:76px;height:21px;border:1px solid #ddd;border-radius:3px;font-size:10px;color:#999;padding:4px 0 0 20px}
.search svg{position:absolute;left:6px;top:5px}
.login{left:658px;top:9px;width:64px;height:20px;background:var(--lime);border-radius:3px;color:#fff;font-weight:700;font-size:10.5px;padding:3px 0 0 9px}
.nav a{position:absolute;top:38px;height:25px;line-height:25px;font-family:Roboto,Arial,sans-serif;font-size:10.5px;color:var(--ink);text-decoration:none}
.nav .active{background:var(--lime);width:56px;text-align:center}

/* hero */
.hero{left:0;top:86px;width:787px;height:257px;background:var(--lime)}
.hero h1{position:absolute;left:0;width:860px;top:70px;text-align:center;font-weight:400;font-size:23px;line-height:30px;color:var(--ink)}
.hero p{position:absolute;left:0;width:860px;top:141px;text-align:center;font-size:12.6px;color:#3a3a10}
.btn{position:absolute;top:180px;height:33px;width:131px;line-height:33px;text-align:center;color:#fff;font-size:11.5px}
.btn-start{left:281px;background:var(--teal)}
.btn-more{left:416px;background:var(--blue)}
.or{position:absolute;left:405px;top:188px;width:19px;height:19px;border-radius:50%;background:#ddd;border:2px solid #fff;font-size:6px;color:#777;text-align:center;line-height:15px}

/* services */
.showcase{left:55px;top:395px;width:380px;height:260px;background:radial-gradient(ellipse at 55% 55%,#e6e6e6 0%,#f4f4f4 55%,#fff 80%)}
.service-icon{position:absolute;width:44px;height:44px;border-radius:50%;border:3px solid #eee;box-shadow:0 1px 3px rgba(0,0,0,.2)}
.service h3{position:absolute;font-weight:400;font-size:9.5px;color:#555;letter-spacing:.2px}
.service p{position:absolute;font-family:Roboto,Arial,sans-serif;font-size:8px;line-height:12px;color:#777}

/* about & blogs */
.section-title{position:absolute;font-size:20px;font-variant:small-caps;color:#333;letter-spacing:.5px;font-weight:400}
.about{left:66px;top:756px;width:392px;font-size:9.6px;line-height:13.1px;letter-spacing:.3px}
.about .lead{color:var(--olive);margin-bottom:3px}
.about .body{color:#555}
.post{position:absolute;left:480px;width:242px}
.post h4{font-weight:400;font-size:9.6px;color:var(--olive);margin-bottom:8px}
.post p{font-size:9.3px;line-height:13px;color:#555}
.post-rule{position:absolute;left:480px;top:840px;width:242px;height:1px;background:var(--rule)}

/* call to action */
.cta{left:65px;top:995px;width:657px;height:76px;background:linear-gradient(105deg,#3a3a3a 0%,#3a3a3a 58%,#2c2c2c 58%,#2c2c2c 100%)}
.cta-dot{position:absolute;left:15px;top:14px;width:50px;height:50px;border:2px solid #111;border-radius:50%;background:var(--lime)}
.cta .l1{position:absolute;left:89px;top:23px;color:#fff;font-family:Roboto,Arial,sans-serif;font-size:12px}
.cta .l2{position:absolute;left:89px;top:44px;color:#fff;font-family:Roboto,Arial,sans-serif;font-size:13.5px}
.start{position:absolute;left:451px;top:18px;width:188px;height:42px;background:var(--lime);border:2px solid #fff;border-radius:3px;padding:3px 0 0 12px;color:#222}
.start b{display:block;font-size:16px;font-weight:700;letter-spacing:.5px}
.start small{display:block;font-size:8px;font-weight:700;margin-top:-1px}
.cta-shadow{left:150px;top:1071px;width:500px;height:10px;background:radial-gradient(ellipse at 50% 0,rgba(0,0,0,.18),transparent 70%)}

/* footer */
.footer{left:0;top:1108px;width:787px;height:92px;background:var(--lime);border-top:4px solid #c9c9c9}
.footer-nav{position:absolute;left:66px;top:32px;font-family:Roboto,Arial,sans-serif;font-size:8.6px;color:#222;word-spacing:2px}
.footer-nav span{color:#444;margin:0 6px}
.copy{position:absolute;left:66px;top:60px;font-family:Roboto,Arial,sans-serif;font-size:8.6px;color:#222}
.sep{position:absolute;left:293px;top:50px;height:28px;border-left:1px dotted #8a9a10}
.social{position:absolute;top:56px;width:19px;height:19px;border-radius:50%}
</style>
</head>
<body>

<header>
  <div class="brand" style="left:66px;top:26px"><span class="brand-dot"></span><span class="brand-name">HALDEN WEB WORKS</span></div>
  <div class="abs search"><svg width="9" height="9" viewBox="0 0 10 10"><circle cx="4" cy="4" r="3" fill="none" stroke="#777" stroke-width="1.3"/><line x1="6.3" y1="6.3" x2="9" y2="9" stroke="#777" stroke-width="1.3"/></svg>search</div>
  <div class="abs login">Login <svg width="7" height="5" viewBox="0 0 7 5" style="margin-left:3px"><path d="M0 1h7L3.5 4.5z" fill="#fff"/></svg></div>
  <nav class="nav">
    <a class="active" style="left:315px">Home</a>
    <a style="left:394px">Blog</a>
    <a style="left:438px">Services</a>
    <a style="left:505px">Packages</a>
    <a style="left:577px">Generic content</a>
    <a style="left:671px">Contact Us</a>
  </nav>
</header>

<section class="abs hero">
  <h1>CUSTOM WEB APPLICATION /<br>DEVELOPMENT</h1>
  <p>LARGE SCALE APPLICATIONS IN THE FINANCIAL, HEALTHCARE, AUTOMOTIVE, AND OTHER INDUSTRIES</p>
  <a class="btn btn-start">GET STARTED</a>
  <a class="btn btn-more">LEARN MORE</a>
  <span class="or">OR</span>
</section>

<section class="services">
  <div class="abs showcase" role="img" aria-label="Laptop showing a dashboard, surrounded by faint social chat bubbles"></div>
  <svg class="abs" style="left:300px;top:420px" width="220" height="230" viewBox="0 0 220 230"><path d="M110 10 A105 105 0 0 1 110 220" fill="none" stroke="#f0f0f0" stroke-width="14"/></svg>

  <div class="service">
    <span class="service-icon" style="left:406px;top:396px;background:var(--purple)"></span>
    <h3 style="left:466px;top:395px">WEB HOSTING CONSULTING</h3>
    <p style="left:467px;top:410px;width:200px">simply dummy text of the printing and typesetting industry. Lorem Ipsum has been the industry's</p>

    <span class="service-icon" style="left:487px;top:450px;background:var(--blue)"></span>
    <h3 style="left:545px;top:453px">CUSTOM APP DEVELOPMENT</h3>
    <p style="left:546px;top:467px;width:160px">simply dummy text of the printing and typesetting industry. Lorem Ipsum has been the industry's</p>

    <span class="service-icon" style="left:494px;top:524px;background:var(--pink)"></span>
    <h3 style="left:548px;top:526px">eVN DEVELOPMENT</h3>
    <p style="left:549px;top:541px;width:160px">simply dummy text of the printing and typesetting industry. Lorem Ipsum has been the industry's</p>

    <span class="service-icon" style="left:442px;top:598px;background:var(--lime-dark)"></span>
    <h3 style="left:500px;top:614px">Quillset DEVELOPMENT</h3>
    <p style="left:501px;top:629px;width:200px">simply dummy text of the printing and typesetting industry. Lorem Ipsum has been the industry's</p>
  </div>
  <div class="abs" style="left:150px;top:692px;width:490px;height:8px;background:radial-gradient(ellipse at 50% 50%,rgba(0,0,0,.05),transparent 70%)"></div>
</section>

<section>
  <h2 class="section-title" style="left:66px;top:724px">About Us</h2>
  <div class="abs about">
    <p class="lead">consectetur adipisicing elit, sed do eiusmod tempor incididunt ut labore et dolore magna aliqua. Ut enim ad minim veniam, quis nostrud exercitation ullamco laboris nisi ut aliquip ex ea commodo consequat. Duis aute irure dolor in reprehenderit in voluptate velit esse</p>
    <p class="body">consectetur adipisicing elit, sed do eiusmod tempor incididunt ut labore et dolore magna aliqua. Ut enim ad minim veniam, quis nostrud exercitation ullamco laboris nisi ut aliquip ex ea commodo consequat. Duis aute irure dolor in reprehenderit in voluptate velit esse cillum dolore eu fugiat nulla pariatur. Excepteur sint occaecat cupidatat non proident, sunt in culpa qui officia deserunt mollit anim id est laborum Duis aute irure dUt enim ad minim veniam, quis nostrud exercitation ullamco laboris nisi ut aliquip ex ea commodo consequat. Duis aute irure dolor in reprehenderit in voluptate velit esse cillum dolore eu fugiat nulla pariatur. Excepteur sint occaecat cupidatat non proident, sunt in culpa qui officia deserunt mollit anim id est laborum Duis aute irure dolor in reprehenderit in voluptate.olor in reprehenderit in voluptate.</p>
  </div>

  <h2 class="section-title" style="left:479px;top:724px">Latest Blogs</h2>
  <article class="post" style="top:757px">
    <h4>Lorem ipsum dolor sit amet</h4>
    <p>Simply dummy text of the printing and typesetting industry. Lorem Ipsum has been the simply dummy text of the printing and typesetting industry.simply dummy text of the printing and typesetting industry. Lorem Ipsum has</p>
  </article>
  <div class="post-rule"></div>
  <article class="post" style="top:852px">
    <h4>Lorem ipsum dolor sit amet</h4>
    <p>Simply dummy text of the printing and typesetting industry. Lorem Ipsum has been the simply dummy text of the printing and typesetting industry.simply dummy text of the printing and typesetting industry. Lorem Ipsum has</p>
  </article>
</section>

<section class="abs cta">
  <span class="cta-dot"></span>
  <p class="l1">We have about 3-4 tiers of services</p>
  <p class="l2">The number of hours versus the monthly invoice total</p>
  <a class="start"><b>START NOW !</b><small>For Lumenix 8, 7, Orbit, Nova (32 &amp; 64 bit)</small></a>
</section>
<div class="abs cta-shadow"></div>

<footer class="abs footer">
  <p class="footer-nav">HOME<span>/</span>ABOUT US<span>/</span>SERVICE<span>/</span>STRENGTH<span>/</span>PARTNER<span>/</span>NEWS<span>/</span>CONTACT US<span>/</span>BLOG</p>
  <p class="copy">Copyright © 2014 All Rights Reserved | Privacy Policy</p>
  <span class="sep"></span>
  <span class="social" style="left:308px;background:#1f4f9c"></span>
  <span class="social" style="left:335px;background:var(--sky)"></span>
  <span class="social" style="left:361px;background:#f08a24"></span>
  <span class="social" style="left:387px;background:#c8c8c8"></span>
  <div class="brand" style="left:533px;top:24px"><span class="brand-dot" style="width:56px;height:56px"></span><span class="brand-name" style="font-size:13.5px;margin-left:6px">HALDEN WEB WORKS</span></div>
</footer>

</body>
</html>
```